Business Card Re-Design/Update

We'd like to update out business cards. I've included our current "Style guide" which has the colour scheme of the organisation in it. I've also included the branding files with logos etc in them.

I've also included a copy of one of our existing cards so that you can see how ugly/dated they look. I'd like a fresh modern corporate look.

Target Market(s)

These are for our clients, potential clients, industry contacts - like all business cards

Contact Information for Business Card

Name
Position
Company Address - Level 1, 47 Garnet Lane, Toowong Qld 4066
Direct Phone
mobile
Email
Website -www.korvalnet.com.au
Logo

Colors

Designer to choose colors to be used in the design.

Requirements
Must have
• Main Logo
• Cards will need to be editable to be able to personalize them for each new employee.
Nice to have
• The MapOUT, HandOVER, UpKEEP would be okay to have if they can be sensibly and professionally added to the look without detracting from the main imagery.
• Maybe they could go on the back of the card? will leave this to your creative discretion as to whether/where they fit.
Should not have
• Should not have decorative or script fonts

```html
<!DOCTYPE html>
<html lang="en">
<head>
<meta charset="utf-8">
<title>korvalnet business cards</title>
<link rel="stylesheet" href="https://fonts.googleapis.com/css2?family=Questrial&display=swap">
<style>
  :root {
    --bg: #2a2a2a;
    --card: #f7f7f7;
    --green: #5f9d3b;
    --blue: #1e88c9;
    --magenta: #a3238f;
    --red: #d42027;
    --ink: #333333;
    --muted: #666666;
    --white: #ffffff;
  }
  * { box-sizing: border-box; margin: 0; padding: 0; }
  html, body {
    width: 1200px; height: 997px; overflow: hidden;
    background: var(--bg);
    font-family: "Questrial", "Century Gothic", sans-serif;
  }
  .card {
    position: absolute;
    width: 620px; height: 354px;
    background: var(--card);
    border-radius: 18px;
    overflow: hidden;
    box-shadow: 0 14px 30px rgba(0,0,0,.45);
  }

  /* brand lockup: one colour, one weight, plain square beside it */
  .brand { display: flex; align-items: center; gap: 16px; }
  .brand-square { width: 30px; height: 30px; background: var(--red); }
  .brand-name { color: var(--ink); font-size: 64px; letter-spacing: 1px; line-height: 1; }

  /* back card */
  .card-back { left: 120px; top: 90px; }
  .service-column { position: absolute; left: 0; top: 0; width: 150px; height: 100%; display: flex; flex-direction: column; }
  .service { flex: 1; display: flex; align-items: flex-end; justify-content: center; padding-bottom: 26px; color: var(--white); font-size: 21px; }
  .service-map { background: var(--green); }
  .service-hand { background: var(--blue); }
  .service-keep { background: var(--magenta); }
  .edge-stripe { position: absolute; right: 0; top: 0; width: 12px; height: 150px; display: flex; flex-direction: column; }
  .edge-stripe span { flex: 1; }
  .card-back .brand { position: absolute; left: 200px; top: 142px; }

  /* front card */
  .card-front { left: 460px; top: 553px; }
  .top-stripe { position: absolute; left: 0; top: 0; width: 100%; height: 10px; display: flex; }
  .top-stripe span, .panel-rule span { flex: 1; }
  .card-front .brand { position: absolute; left: 0; right: 0; top: 48px; justify-content: center; }
  .staff-row {
    position: absolute; left: 32px; right: 32px; top: 140px;
    display: flex; justify-content: space-between; align-items: flex-end;
    color: var(--ink);
  }
  .staff-name { font-size: 19px; line-height: 1.2; }
  .staff-position { font-size: 13px; color: var(--muted); line-height: 1.4; }
  .address { font-size: 13px; color: var(--muted); text-align: right; line-height: 1.4; }
  .panel-rule { position: absolute; left: 0; bottom: 122px; width: 100%; height: 4px; display: flex; }
  .contact-row { position: absolute; left: 0; bottom: 0; width: 100%; height: 115px; display: flex; }
  .contact { flex: 1; display: flex; flex-direction: column; align-items: center; justify-content: center; gap: 10px; color: var(--ink); font-size: 14px; line-height: 1.4; text-align: center; }
  .contact-phone { background: var(--green); }
  .contact-mail { background: var(--blue); }
  .contact-web { background: var(--magenta); }
  .icon { width: 24px; height: 24px; }
  .green { background: var(--green); }
  .blue { background: var(--blue); }
  .magenta { background: var(--magenta); }
</style>
</head>
<body>

<section class="card card-back" aria-label="Card back">
  <div class="service-column">
    <div class="service service-map">MapOUT</div>
    <div class="service service-hand">HandOVER</div>
    <div class="service service-keep">UpKEEP</div>
  </div>
  <div class="edge-stripe"><span class="green"></span><span class="blue"></span><span class="magenta"></span></div>
  <div class="brand">
    <span class="brand-square"></span>
    <span class="brand-name">korvalnet</span>
  </div>
</section>

<section class="card card-front" aria-label="Card front">
  <div class="top-stripe"><span class="green"></span><span class="blue"></span><span class="magenta"></span></div>
  <div class="brand">
    <span class="brand-square"></span>
    <span class="brand-name">korvalnet</span>
  </div>
  <div class="staff-row">
    <div class="staff">
      <p class="staff-name">Full Name</p>
      <p class="staff-position">Position Title</p>
    </div>
    <p class="address">Level 1, 47 Garnet Lane<br>Toowong Qld 4066</p>
  </div>
  <div class="panel-rule"><span class="green"></span><span class="blue"></span><span class="magenta"></span></div>
  <div class="contact-row">
    <div class="contact contact-phone">
      <svg class="icon" viewBox="0 0 24 24" aria-hidden="true">
        <circle cx="12" cy="12" r="12" fill="#fff"/>
        <path d="M8 7h2l1 3-1.3 1a7 7 0 0 0 3.3 3.3l1-1.3 3 1v2a1.5 1.5 0 0 1-1.6 1.5A10 10 0 0 1 6.5 8.6 1.5 1.5 0 0 1 8 7z" fill="#d42027"/>
      </svg>
      <p>1300 555 016<br>+61 7 3000 0147</p>
    </div>
    <div class="contact contact-mail">
      <svg class="icon" viewBox="0 0 24 24" aria-hidden="true">
        <circle cx="12" cy="12" r="12" fill="#fff"/>
        <rect x="6" y="8" width="12" height="8" fill="none" stroke="#d42027" stroke-width="1.5"/>
        <path d="M6 8l6 5 6-5" fill="none" stroke="#d42027" stroke-width="1.5"/>
      </svg>
      <p>enquiry@korvalnet.com.au</p>
    </div>
    <div class="contact contact-web">
      <svg class="icon" viewBox="0 0 24 24" aria-hidden="true">
        <circle cx="12" cy="12" r="12" fill="#fff"/>
        <circle cx="12" cy="12" r="6" fill="none" stroke="#d42027" stroke-width="1.5"/>
        <path d="M6 12h12M12 6c-3 3.5-3 8.5 0 12M12 6c3 3.5 3 8.5 0 12" fill="none" stroke="#d42027" stroke-width="1.2"/>
      </svg>
      <p>www.korvalnet.com.au</p>
    </div>
  </div>
</section>

</body>
</html>
```